Business Card Design Project for Female Personal Trainer

I need a business card design to appeal to female clients for my personal training and group fitness boot camp business called 'Lumeva Studios'. It should be girly, fun and have an active/healthy pic or figure incorporated into the business name.

Target Market(s)

- Females 20-65yrs

Industry/Entity Type

Training

Font styles to use
Serif
Sans Serif

Colors
e34197
e567a6

Requirements
Must have
• First Side of Business Card Details :

Corin Delph
MASTER PERSONAL TRAINER
Cert III & Cert IV in Fitness
Senior First Aid
Mobile: 0438 507 164
Email: lumeva@quillpost.net
Facebook: Lumeva Studios

* Mobile Personal Training *Individual Sessions *Bootcamp *Weight-loss and Toning

Second Side of Business Card I want to offer a free personal consult:
Something like this:

Need direction with your health & fitness goals?

Call now for your free 1 on 1 Personal Training Session with full consultation

Nice to have
• Have a sub-heading for example:

'Promoting healthy living through fitness & nutrition'

- have the colour pink or blue (to appeal to a female)

- a picture/motif//logo attached (sometimes a picture paints a thousand words)

Should not have
• * picture of a person with big muscles or appeal to a man (I'm training women only)

* should not be busy or crammed up look (if I've added to much info above please just use to your discretion).

```html
<!DOCTYPE html>
<html lang="en">
<head>
<meta charset="utf-8">
<title>Lumeva Studios – Business Card</title>
<link rel="stylesheet" href="https://fonts.googleapis.com/css2?family=Open+Sans:wght@400;700;800&display=swap">
<style>
  :root {
    --backdrop: #3b2517;
    --card-white: #ffffff;
    --pink: #e34197;
    --pink-soft: #e567a6;
    --blue: #1c7cc2;
    --ink: #111111;
    --text-font: "Open Sans", Arial, sans-serif;
  }
  * { box-sizing: border-box; margin: 0; padding: 0; }
  html, body {
    width: 1200px; height: 1000px; overflow: hidden;
    background: var(--backdrop);
    font-family: var(--text-font);
  }
  .canvas { position: relative; width: 1200px; height: 1000px; }
  .card {
    position: absolute; width: 740px; height: 420px;
    background: var(--card-white);
    overflow: hidden;
    box-shadow: 0 8px 24px rgba(0,0,0,0.45);
  }
  .card--front { left: 50px; top: 40px; }
  .card--back { left: 410px; top: 530px; }

  /* Front side */
  .brand-name {
    font-family: var(--text-font);
    font-weight: 800;
    color: var(--pink);
    letter-spacing: -1px;
    line-height: 1;
    white-space: nowrap;
  }
  .card--front .brand-name {
    position: absolute; left: 62px; top: 118px; font-size: 46px;
  }
  .services {
    position: absolute; left: 462px; top: 62px;
    list-style: none; color: var(--blue); font-size: 16px; line-height: 25px;
  }
  .services li::before {
    content: ""; display: inline-block; width: 6px; height: 6px;
    border-radius: 50%; background: var(--pink);
    margin-right: 7px; vertical-align: middle;
  }
  .trainer { position: absolute; left: 100px; top: 288px; }
  .trainer__name { color: var(--pink); font-size: 34px; font-weight: 400; line-height: 1.1; margin-bottom: 6px; }
  .trainer__detail { color: var(--blue); font-size: 16px; line-height: 30px; }
  .trainer__title { text-transform: uppercase; }
  .contact { position: absolute; left: 470px; top: 294px; list-style: none; font-size: 19px; line-height: 31px; }
  .contact__label { color: var(--blue); display: inline-block; width: 28px; }
  .contact__value { color: var(--pink); }

  /* Back side */
  .band { position: absolute; left: 0; width: 100%; }
  .band--blue { top: 0; height: 218px; background: var(--blue); }
  .band--stripe { top: 92px; height: 10px; background: var(--card-white); }
  .band--white { top: 218px; height: 76px; background: var(--card-white); }
  .band--pink { top: 294px; height: 126px; background: var(--pink-soft); }
  .logo-pill {
    position: absolute; left: 205px; top: 42px; width: 330px; height: 112px;
    background: var(--card-white); border-radius: 56px;
    display: flex; align-items: center; justify-content: center;
  }
  .logo-pill .brand-name { font-size: 40px; }
  .question {
    position: absolute; top: 236px; width: 100%; text-align: center;
    color: var(--pink); font-size: 26px;
  }
  .offer {
    position: absolute; top: 318px; width: 100%; text-align: center;
    color: var(--ink); font-size: 25px; font-weight: 700; line-height: 32px;
  }
</style>
</head>
<body>
<main class="canvas">
  <section class="card card--front" aria-label="Business card front">
    <div class="brand-name">Lumeva Studios</div>
    <ul class="services">
      <li>Mobile Personal Training</li>
      <li>Individual Sessions</li>
      <li>Bootcamp</li>
      <li>Weight-loss and Toning</li>
    </ul>
    <div class="trainer">
      <h1 class="trainer__name">Corin Delph</h1>
      <p class="trainer__detail trainer__title">Master Personal Trainer</p>
      <p class="trainer__detail">Cert III &amp; Cert IV in Fitness</p>
      <p class="trainer__detail">Senior First Aid</p>
    </div>
    <ul class="contact">
      <li><span class="contact__label">m:</span><span class="contact__value">0438 507 164</span></li>
      <li><span class="contact__label">e:</span><span class="contact__value">lumeva@quillpost.net</span></li>
      <li><span class="contact__label">f:</span><span class="contact__value">Lumeva Studios</span></li>
    </ul>
  </section>

  <section class="card card--back" aria-label="Business card back">
    <div class="band band--blue"></div>
    <div class="band band--stripe"></div>
    <div class="band band--white"></div>
    <div class="band band--pink"></div>
    <div class="logo-pill"><span class="brand-name">Lumeva Studios</span></div>
    <p class="question">Need direction with your health &amp; fitness goals?</p>
    <p class="offer">Call Now for Your FREE 1 on 1 Personal Training<br>Session with Full Consultation!</p>
  </section>
</main>
</body>
</html>
```